Clerical Business Card Design

I have just started a new business focusing on Clerical / Administration Support for Small to Medium sized Businesses. I can provide support not just only my local area but anywhere as long as it is able to be done over the internet/email. I am the only person working in the business.
I would like to see some designs that are bright in colour yet a clean fresh design. The design should communicate balance.
Updates

Target Market(s)

Small to Medium sized Professional Businesses

Industry/Entity Type

Business

Contact Information for Business Card

Business Name: Vormley's Clerical
Statement: Delivering Steady Reliable Assistance
My Name: Ilsa Vormley
Phone: 0418 571 924 or 02 6519 4027
Email: vormleysclerical@plimmet.com.au

Colors

Designer to choose colors to be used in the design.

Requirements
Must have
• I'm open to suggestions
Nice to have
• I would like to see maybe something done with the two "C" in the business name whether that could be a focus of difference
Should not have
• Cartoon type pictures

```html
<!DOCTYPE html>
<html lang="en">
<head>
<meta charset="utf-8">
<title>Vormley's Clerical – Business Card</title>
<link rel="stylesheet" href="https://fonts.googleapis.com/css2?family=Tinos&family=Noto+Sans&display=swap">
<style>
  :root {
    --paper: #ffffff;
    --accent-green: #9bc93b;
    --brand-grey: #808285;
    --name-ink: #1f1f1f;
    --detail-grey: #8a8b8d;
    --number-grey: #58595b;
    --rule-grey: #b9babc;
  }
  html, body {
    margin: 0;
    padding: 0;
    overflow: hidden;
    background: var(--paper);
  }
  .card {
    position: relative;
    width: 1200px;
    height: 741px;
    background: var(--paper);
    overflow: hidden;
    font-family: "Tinos", "Times New Roman", serif;
  }
  .brand-mark {
    position: absolute;
    left: 506px;
    top: 322px;
    width: 60px;
    height: 60px;
    border-radius: 50%;
    background: var(--accent-green);
  }
  .brand-name {
    position: absolute;
    left: 580px;
    top: 312px;
    margin: 0;
    font-size: 49px;
    font-weight: 400;
    line-height: 1;
    color: var(--brand-grey);
    white-space: nowrap;
  }
  .brand-tagline {
    position: absolute;
    left: 588px;
    top: 364px;
    margin: 0;
    font-size: 34px;
    font-weight: 400;
    line-height: 1;
    color: var(--brand-grey);
    white-space: nowrap;
  }
  .contact-rule {
    position: absolute;
    left: 549px;
    top: 532px;
    width: 1px;
    height: 129px;
    background: var(--rule-grey);
  }
  .contact-block {
    position: absolute;
    left: 583px;
    top: 522px;
  }
  .contact-name {
    margin: 0 0 12px;
    font-size: 41px;
    font-weight: 400;
    line-height: 1.1;
    color: var(--name-ink);
    white-space: nowrap;
  }
  .contact-line {
    margin: 0;
    font-size: 31px;
    line-height: 1.42;
    color: var(--detail-grey);
    white-space: nowrap;
  }
  .contact-label {
    margin-right: 8px;
  }
  .phone-number {
    font-family: "Noto Sans", Arial, sans-serif;
    font-size: 25px;
    color: var(--number-grey);
    letter-spacing: 0.5px;
  }
  .email-address {
    font-size: 30px;
  }
</style>
</head>
<body>
  <main class="card">
    <span class="brand-mark" aria-hidden="true"></span>
    <h1 class="brand-name">Vormley's Clerical Solutions</h1>
    <p class="brand-tagline">Delivering Steady Reliable Assistance</p>

    <div class="contact-rule" aria-hidden="true"></div>
    <section class="contact-block">
      <h2 class="contact-name">Ilsa Vormley</h2>
      <p class="contact-line"><span class="contact-label">Phone:</span><span class="phone-number">0418 571 924</span> or <span class="phone-number">02 6519 4027</span></p>
      <p class="contact-line"><span class="contact-label">Email:</span><span class="email-address">vormleysclerical@plimmet.com.au</span></p>
    </section>
  </main>
</body>
</html>
```